Marketing One-Sheet for Security Deposit Claim Notice

I need a one-sheet flyer formatted for email distribution — optimized as a JPEG/PNG that I can insert into Constant Contact or Outlook. I do not want to attach it to an email, but insert it in the email we send out. I would like it to look professional but engaging. Some images would be good, but want to make sure it reads well if images do not load for the recipients. The text is in the attached Word document, but I am open to changes/ideas that may be better for marketing purposes. I included the URLs for some of the links I would like in the one-sheet that is clickable. The logo for the business is being uploaded on the Word document. Proposed text is also uploaded in a Word document. Thank you.

Target Market(s)

Landlords, Real Estate Agents, Property Managers

Industry/Entity Type

Legal

Requirements
Must have
• Professional but appealing design. The One-sheet is going to be placed in the body of emails, not as an attachment.
Nice to have
• Include our logo for the business and the web links please.
Should not have
• Images can be ok, but it needs to look right if images do not download from the email sent out.

```html
<!DOCTYPE html>
<html lang="en">
<head>
<meta charset="utf-8">
<title>Security Deposit Claim Notice – Harbor Lease Legal</title>
<link href="https://fonts.googleapis.com/css2?family=Poppins:wght@300;400;500;600;700;800&display=swap" rel="stylesheet">
<style>
  :root {
    --red: #e0202a;
    --deep-red: #b3161c;
    --ink: #111111;
    --body: #2a2a2a;
    --grey-band: #f3f3f3;
    --white: #ffffff;
  }
  * { box-sizing: border-box; margin: 0; padding: 0; }
  html, body { width: 1200px; height: 5343px; overflow: hidden; background: var(--white); }
  body { position: relative; font-family: 'Poppins', sans-serif; color: var(--body); }
  .abs { position: absolute; }

  /* Brand */
  .brand { left: 0; width: 1200px; top: 105px; text-align: center; }
  .brand-row { display: inline-flex; align-items: center; gap: 18px; }
  .brand-name { font-size: 54px; font-weight: 600; color: var(--red); letter-spacing: 2px; line-height: 1; }
  .brand-mark { width: 58px; height: 58px; background: var(--red); }
  .brand-tag { font-size: 19px; color: var(--deep-red); margin-top: 10px; line-height: 1.2; }
  .brand-contact { font-size: 27px; font-weight: 600; color: var(--deep-red); line-height: 1.3; margin-top: 8px; }

  /* Headline */
  .headline { left: 0; width: 1200px; top: 415px; text-align: center; font-weight: 700; letter-spacing: -2px; line-height: 1.08; }
  .headline .dark { color: var(--ink); font-size: 64px; display: block; }
  .headline .accent { color: var(--red); font-size: 82px; display: block; margin-top: 8px; }

  /* Red band */
  .red-band { left: 0; top: 1074px; width: 1200px; height: 912px; background: linear-gradient(180deg, #e82430 0%, #d51c25 60%, #c8161e 100%); }
  .hero-house { left: 130px; top: 736px; width: 940px; height: 632px; border-radius: 8px;
    background: linear-gradient(180deg, #d9d9d9 0%, #a9a9a9 55%, #5c5c5c 100%); }

  .req-title { left: 0; width: 1200px; top: 1420px; text-align: center; color: var(--white); font-size: 56px; font-weight: 600; line-height: 1.12; letter-spacing: -1px; }
  .req-card { top: 1648px; width: 346px; height: 222px; background: var(--white); border-radius: 6px;
    display: flex; align-items: center; justify-content: center; text-align: center; padding: 30px 24px 0;
    font-size: 36px; line-height: 1.25; color: var(--ink); box-shadow: 0 4px 14px rgba(0,0,0,.18); }
  .req-check { top: 1597px; width: 82px; height: 82px; border-radius: 50%; background: #222; display: flex; align-items: center; justify-content: center; }

  /* Hands photo */
  .hands-photo { left: 0; top: 1986px; width: 1200px; height: 547px;
    background: linear-gradient(90deg, #c98a2c 0%, #8a5a3a 35%, #5a4a42 65%, #3d3f44 100%); }

  /* Consequences */
  .cons-title { left: 0; width: 1200px; top: 2618px; text-align: center; font-size: 48px; line-height: 1.3; color: var(--ink); letter-spacing: -0.5px; }
  .cons-divider { left: 599px; top: 2794px; width: 3px; height: 233px; background: var(--red); }
  .cons-item { top: 2800px; width: 440px; text-align: center; font-size: 33px; line-height: 1.27; font-weight: 300; color: var(--body); text-transform: none; }
  .cons-item svg { display: block; margin: 0 auto 22px; }

  /* Grey band */
  .grey-band { left: 0; top: 3105px; width: 1200px; height: 461px; background: var(--grey-band); }
  .copy { font-size: 35px; line-height: 1.22; color: var(--ink); font-weight: 300; letter-spacing: -0.4px; }
  .photo-frame { border: 3px solid var(--red); border-radius: 8px; }
  .family-photo-a { left: 657px; top: 3180px; width: 456px; height: 431px; background: linear-gradient(160deg, #ece7e2 0%, #c9b8a6 55%, #8f6c5a 100%); }
  .family-photo-b { left: 87px; top: 3667px; width: 456px; height: 431px; background: linear-gradient(160deg, #f1efec 0%, #cdbba3 50%, #9a8066 100%); }

  /* Pricing */
  .black-band { left: 0; top: 4328px; width: 1200px; height: 346px; background: var(--ink); }
  .price-tag { left: 325px; top: 4229px; width: 550px; height: 145px; background: var(--deep-red); border-radius: 4px;
    display: flex; align-items: center; justify-content: center; color: var(--white); font-size: 70px; font-weight: 600; letter-spacing: -1px; }
  .price-desc { left: 0; width: 1200px; top: 4405px; text-align: center; color: var(--white); font-size: 56px; line-height: 1.12; letter-spacing: -1px; }
  .price-alt { left: 325px; top: 4602px; width: 550px; height: 145px; background: var(--white); border: 2px solid #e8a0a3; border-radius: 4px;
    display: flex; align-items: center; justify-content: center; gap: 22px; }
  .price-alt .amount { color: var(--red); font-size: 76px; font-weight: 600; letter-spacing: -1px; }
  .price-alt .note { font-size: 33px; line-height: 1.2; color: var(--body); }

  .cta { left: 270px; top: 4855px; width: 661px; height: 145px; background: var(--ink); border-radius: 10px;
    display: flex; align-items: center; justify-content: center; color: var(--white); font-size: 56px; letter-spacing: -1px; text-decoration: none; }
  .contact-link { left: 0; width: 1200px; top: 5058px; text-align: center; color: var(--deep-red); font-size: 51px; line-height: 1.42; letter-spacing: -0.5px; }
  .contact-link a { color: inherit; text-decoration: underline; text-underline-offset: 8px; text-decoration-thickness: 3px; }
</style>
</head>
<body>

<header class="brand abs">
  <div class="brand-row">
    <span class="brand-name">HARBOR LEASE LEGAL</span>
    <span class="brand-mark"></span>
  </div>
  <p class="brand-tag">a Legal Resource for Landlords,<br>Investors &amp; Property Managers</p>
  <p class="brand-contact">HarborLeaseLegal.com<br>1(800) 555-0142</p>
</header>

<h1 class="headline abs">
  <span class="dark">LANDLORD, NEED<br>TO KEEP THE</span>
  <span class="accent">SECURITY DEPOSIT?</span>
</h1>

<div class="red-band abs"></div>
<div class="hero-house abs" role="img" aria-label="Modern two-storey rental house with landscaped entry steps"></div>

<h2 class="req-title abs">Security Deposit<br>Claim Notice requirements</h2>

<div class="req-card abs" style="left:56px">Must be served on time</div>
<div class="req-card abs" style="left:427px">Must be served according to Florida law</div>
<div class="req-card abs" style="left:798px">Must contain specific wording</div>
<div class="req-check abs" style="left:188px"><svg width="40" height="30" viewBox="0 0 40 30"><path d="M4 15 L15 26 L36 4" fill="none" stroke="#fff" stroke-width="4"/></svg></div>
<div class="req-check abs" style="left:559px"><svg width="40" height="30" viewBox="0 0 40 30"><path d="M4 15 L15 26 L36 4" fill="none" stroke="#fff" stroke-width="4"/></svg></div>
<div class="req-check abs" style="left:930px"><svg width="40" height="30" viewBox="0 0 40 30"><path d="M4 15 L15 26 L36 4" fill="none" stroke="#fff" stroke-width="4"/></svg></div>

<div class="hands-photo abs" role="img" aria-label="Cupped hands holding a small model house in warm light"></div>

<h2 class="cons-title abs">Security Deposit Claim<br>Notice not correct, then</h2>

<div class="cons-item abs" style="left:131px">
  <svg width="76" height="72" viewBox="0 0 76 72" aria-hidden="true">
    <circle cx="48" cy="24" r="20" fill="#e0202a"/>
    <text x="48" y="33" text-anchor="middle" font-family="Poppins, sans-serif" font-size="24" font-weight="700" fill="#fff">$</text>
    <rect x="4" y="44" width="14" height="26" fill="#e0202a"/>
    <path d="M20 48 H44 L66 42 Q72 42 70 50 L48 66 H20 Z" fill="#e0202a"/>
  </svg>
  Tenant could demand return of FULL SECURITY DEPOSIT
</div>
<div class="cons-divider abs"></div>
<div class="cons-item abs" style="left:630px">
  <svg width="80" height="76" viewBox="0 0 80 76" aria-hidden="true">
    <g fill="#e0202a">
      <rect x="18" y="6" width="30" height="18" rx="3" transform="rotate(40 33 15)"/>
      <rect x="36" y="26" width="36" height="9" rx="3" transform="rotate(40 54 30)"/>
      <rect x="8" y="56" width="50" height="8" rx="2"/>
      <rect x="2" y="66" width="62" height="8" rx="2"/>
    </g>
  </svg>
  Tenant can sue and recover LEGAL FEES FROM THE LANDLORD
</div>

<div class="grey-band abs"></div>
<p class="copy abs" style="left:89px; top:3165px; width:500px">There are lawyers that specialize in representing TENANTS against landlords for not making a proper claim on the security deposit. They can win the case and recover thousands of dollars $$ in legal fees from the Landlord.</p>
<div class="family-photo-a photo-frame abs" role="img" aria-label="Family of three sitting on the floor at home, parents forming a roof over their daughter"></div>

<div class="family-photo-b photo-frame abs" role="img" aria-label="Family sitting on a living room floor holding a cardboard roof above their child"></div>
<p class="copy abs" style="left:603px; top:3710px; width:540px">Plus, the tenant can get back 100% of the Security Deposit, even if they owe the Landlord unpaid rent or caused damages to the property. Florida law helps the tenants if the Security Deposit Claim Notice is not served on time and correctly.</p>

<div class="black-band abs"></div>
<div class="price-tag abs">$350 Flat Fee</div>
<p class="price-desc abs">to prepare and serve Security<br>Deposit Claim Notices for Landlords.</p>
<div class="price-alt abs">
  <span class="amount">$450</span>
  <span class="note">for commercial<br>properties</span>
</div>

<a class="cta abs" href="#">For More Information</a>
<p class="contact-link abs"><a href="#">Contact Us to prepare the<br>Security Deposit Claim Notice.</a></p>

</body>
</html>
```